Poster for a Bicycle show/Expo

We need a poster for a Bicycle show/Expo and sustainable transport. Exhibitors will sell bikes, cycling clothing, accessories, etc. ...
This show is annual and the Poster is for the 2015 edition.

The style must be modern, dynamic, bright colors.

Your concept must be compatible in a landscape format. (We will ourselves adaptations of different formats.)
Width: 210 mm
Height: 297 mm
It's necessary for us to have the source file (vector) for make, later, the different format (flyers, website, ...)

Content of the Poster:
- 1 big picture (no clip art)
- Big title: « Fête Roulix » (« Salon » or « Salon du » can be small and « Vélo » big.)
- Subtitle: « et de la mobilité douce »
- Date: « 8, 9 et 10 mai 2015 » or « 8-10 mai 2015 »
- Place: « Halle TRX - Quai Brenaz »
- Text line 1: « www.fete-roulix.ch - Entrée gratuite »
- Text line 2« Piste d’essais - Restauration sur place »
- Text line 3: « Ve 8 mai de 17h à 21h - Sa 9 mai de 10h à 20h - Di 10 mai de 10h à 18h »
- Please, leave a zone in the poster for sponsors logos
(The predominant information (most visible) are: « Fête Roulix » and « 8, 9 et 10 mai 2015 or 8-10 mai 2015 »)

Content of the big picture:
- from a cheap stock, like PixoBanq.com
- a bicycle in action or a detail of a bicycle (or a accessory) (no race bike)
- a modern picture with bright colors.
- if a person is on the picture, we prefer a men
- not an aerial view with cyclists in a landscape.

Some examples of poster of shows - with typo-title worked

http://www.bassinexpoville.com/Temp/IMG/F_a7c2e9b4d1f0836255e1b7a9c4d3f2e6812c9b0a4e5f7_200_296.png

http://qz4m.tolvanfoires.fr/Data/kmtolv_mer/block/F_9bd1c3e7f2a4605813c9e2d7b4a8f6c0d3e1a527f86c2.pdf
(page 2 of this PDF)

http://salons.marvelle-agenda.fr/images/marvelle-agenda/foires-salons/phototheque/expo-moto-brivanne/expo-moto-brivanne2012-affiche.jpg

http://www.drupaix.net/blog/wp-content/uploads/2007/03/affiche-foire-des-pages.jpg

http://www.voilemarine-club.com/wp-content/affiche-regate-2007.jpg

Hello,

For information, for your next versions, please, add the text "Piste d'essais".

- Text line 1: « www.fete-roulix.ch - Entrée gratuite »
- Text line 2: « Piste d’essais - Restauration sur place »
- Text line 3: « Ve 8 mai de 17h à 21h - Sa 9 mai de 10h à 20h - Di 10 mai de 10h à 18h »

Thanks,
Mathieu

Landscape

Sans Serif

```html
<!DOCTYPE html>
<html lang="fr">
<head>
<meta charset="utf-8">
<title>Fête Roulix et de la mobilité douce</title>
<link href="https://fonts.googleapis.com/css2?family=Bebas+Neue&family=Oswald:wght@400;500&display=swap" rel="stylesheet">
<style>
  :root {
    --ink: #111111;
    --paper: #f7f7f5;
    --base: #1c1c24;
    --sun: #ffd23f;
    --tangerine: #ff7a3d;
    --berry: #e8336d;
    --lagoon: #1fb5c4;
    --sponsor-slot: #3a3a44;
  }
  html, body {
    margin: 0;
    padding: 0;
    overflow: hidden;
    background: var(--paper);
  }
  .poster {
    position: relative;
    width: 853px;
    height: 1200px;
    overflow: hidden;
    background: var(--base);
  }
  .hero-photo {
    position: absolute;
    left: 0;
    top: 0;
    width: 853px;
    height: 830px;
    background:
      radial-gradient(ellipse at 68% 20%, var(--sun) 0%, transparent 50%),
      radial-gradient(ellipse at 15% 70%, var(--lagoon) 0%, transparent 55%),
      linear-gradient(160deg, var(--tangerine) 0%, var(--berry) 55%, var(--base) 100%);
  }
  .info-band {
    position: absolute;
    left: 0;
    top: 790px;
    width: 853px;
    height: 330px;
  }
  .info-band svg {
    position: absolute;
    inset: 0;
  }
  .info-text {
    position: absolute;
    inset: 0;
    color: var(--ink);
    text-transform: uppercase;
  }
  .title {
    position: absolute;
    left: 28px;
    top: 36px;
    margin: 0;
    font-family: "Bebas Neue", sans-serif;
    font-weight: 400;
    font-size: 140px;
    line-height: 0.82;
    letter-spacing: 1px;
    white-space: nowrap;
  }
  .subtitle {
    position: absolute;
    left: 30px;
    top: 156px;
    margin: 0;
    font-family: "Bebas Neue", sans-serif;
    font-weight: 400;
    font-size: 52px;
    line-height: 1;
    white-space: nowrap;
  }
  .when-where {
    position: absolute;
    left: 30px;
    top: 222px;
    margin: 0;
    font-family: "Oswald", sans-serif;
    font-weight: 500;
    font-size: 24px;
    line-height: 1.15;
    white-space: nowrap;
  }
  .details {
    position: absolute;
    left: 318px;
    top: 232px;
    margin: 0;
    font-family: "Oswald", sans-serif;
    font-weight: 400;
    font-size: 16px;
    line-height: 1.3;
    letter-spacing: 0.2px;
    white-space: nowrap;
  }
  .sponsor-zone {
    position: absolute;
    left: 28px;
    top: 1134px;
    width: 797px;
    height: 50px;
    display: flex;
    gap: 14px;
  }
  .sponsor-slot {
    flex: 1;
    background: var(--sponsor-slot);
  }
</style>
</head>
<body>
<main class="poster">
  <div class="hero-photo" role="img" aria-label="Photo aux couleurs vives d'un guidon chromé de vélo et de son tube de direction, en gros plan"></div>

  <section class="info-band">
    <svg width="853" height="330" viewBox="0 0 853 330" aria-hidden="true">
      <polygon fill="var(--paper)" points="0,14 60,8 120,16 190,6 260,12 330,4 400,14 470,8 540,16 610,6 680,12 750,4 810,14 853,10 853,318 800,324 720,316 640,326 560,318 480,328 400,320 320,326 240,318 160,326 80,320 0,324"/>
    </svg>
    <div class="info-text">
      <h1 class="title">Fête Roulix</h1>
      <p class="subtitle">Et de la mobilité douce</p>
      <p class="when-where">8, 9 et 10 mai 2015<br>Halle TRX - Quai Brenaz</p>
      <p class="details">
        Piste d'essais · Restauration sur place<br>
        www.fete-roulix.ch · Entrée gratuite<br>
        Ve 8 mai de 17h à 21h · Sa 9 mai de 10h à 20h · Di 10 mai de 10h à 18h
      </p>
    </div>
  </section>

  <footer class="sponsor-zone" aria-label="Espace partenaires">
    <div class="sponsor-slot"></div>
    <div class="sponsor-slot"></div>
    <div class="sponsor-slot"></div>
    <div class="sponsor-slot"></div>
    <div class="sponsor-slot"></div>
  </footer>
</main>
</body>
</html>
```